Веб-сайт для застройщика под греческую золотую визу Veltaroon.gr
застройщик под греческую золотую визу Veltaroon.gr
Veltaroon.gr
https://morvilo-estates.com/
https://tpk.example/
Veltaroon Development IKE — Website Design Brief
Домен: veltaroon.gr
Название Veltaroon является авторским сочетанием слов:
Hellenic
Premium
Название должно ассоциироваться с:
premium Mediterranean lifestyle
boutique investment real estate
комфортом и эстетикой
Это можно опционально и ненавязчиво обыгрывать в дизайне:
через typography
через premium визуальные акценты
через Mediterranean aesthetic
через сочетание natural + premium visual language
Важно:
Бренд не должен выглядеть overly luxury или “gold-plated wealth style”.
Основной акцент:
tasteful premium
calm confidence
boutique sophistication
1. О компании
Veltaroon Development IKE — девелоперская компания в Греции, которая занимается:
покупкой и реновацией зданий
созданием boutique apartments
продажей недвижимости под Greek Golden Visa
дальнейшим управлением арендой для инвесторов
2. Основная идея сайта
Главный акцент:
Greek Golden Visa
инвестиции в недвижимость в Греции
получение ВНЖ в Европе
комфортный Mediterranean lifestyle
Важно показать, что компания делает проекты «с душой»:
натуральные материалы
светлое дерево
мягкий olive green
уютные современные интерьеры
boutique Mediterranean aesthetics
3. Сайт должен выглядеть
premium
trustworthy
modern
investment-oriented
4. Сайт НЕ должен выглядеть
как агентство недвижимости
как дешёвый Golden Visa landing page
как обычная строительная компания
5. Целевая аудитория
Средний возраст клиентов: 45+ лет, семейные инвесторы, часто ищущие решение для всей семьи.
Инвесторы и семьи из:
Китай
Турция
СНГ
Middle East
Основная цель клиентов:
получение ВНЖ в Европе через Greek Golden Visa
покупка доходной недвижимости
инвестиции в недвижимость в ЕС
6. Основное меню
Greek Golden Visa или просто Golden Visa
Projects
Investors
Partners
Contact (внутри Contact раздела будет вставка About Us либо же вставка будет сразу на главной странице - на ваше усмотрение)
Дополнительно:
Client Login (отдельный кабинет для покупателей квартир / инвесторов)
7. Языки сайта
EN (по умолчанию)
GR
RU
中文
TR
8. Визуальная стилистика
Эстетика
Mediterranean vibe
boutique living vibe
premium natural materials
Цвета:
olive green
warm white
beige
soft stone grey
(Цвета даны справочно и могут адаптироваться дизайнером)
UI стиль:
clean
calm
ВАЖНО:
Полное техническое задание не влезло в описание и размещено в открытом виде на внешнем файлообменнике в текстовом файле:
https://filebarrow.example/k4Rq8
или
https://sklad-faylov.example/7pLmz

```html
<!DOCTYPE html>
<html lang="en">
<head>
<meta charset="utf-8">
<title>Veltaroon Development — Greek Golden Visa</title>
<link rel="stylesheet" href="https://fonts.googleapis.com/css2?family=Cormorant+Garamond:ital,wght@0,400;0,500;1,400;1,500&family=Inter:wght@400;500;600&display=swap">
<style>
:root{
  --olive:#3f4a35;
  --olive-card:#4a5540;
  --dark:#2f2c28;
  --beige:#f4efe8;
  --sand:#e9dfd1;
  --warm:#fbf8f3;
  --tan:#c6a07a;
  --tan-dark:#a88360;
  --ink:#2a2824;
  --muted:#6d665d;
  --line:#d9d0c4;
  --stone:#d8d2ca;
}
*{box-sizing:border-box;margin:0;padding:0}
html,body{width:1200px;height:4025px;overflow:hidden}
body{font-family:"Inter",sans-serif;color:var(--ink);background:var(--beige);position:relative;font-size:13px}
em{font-style:italic}
section,header,footer{position:absolute;left:0;width:1200px}
.label{font-size:10.5px;letter-spacing:2px;text-transform:uppercase;color:var(--muted)}
.btn{display:inline-flex;align-items:center;justify-content:center;gap:12px;font-size:11px;letter-spacing:.6px;text-transform:uppercase;height:54px}
.arrow{width:20px;height:8px}

/* header */
.site-header{top:8px;left:8px;width:1184px;height:80px;background:rgba(251,248,243,.85);display:flex;align-items:center;padding:0 84px;z-index:3}
.brand{display:flex;align-items:center;gap:10px}
.brand-mark{width:34px;height:34px;border:1.5px solid var(--ink)}
.brand-name{font-family:"Cormorant Garamond",serif;font-size:22px;font-weight:500;letter-spacing:1px;color:var(--ink)}
.nav{display:flex;gap:36px;margin-left:104px;font-size:12.5px}
.login{margin-left:auto;border:1px solid var(--ink);height:40px;width:140px;display:flex;align-items:center;justify-content:center;gap:8px;font-size:11px}
.lang{margin-left:42px;font-size:11px}

/* hero */
.hero{top:0;height:800px;background:var(--beige)}
.hero-photo{position:absolute;left:560px;top:0;width:640px;height:800px;background:linear-gradient(100deg,var(--beige) 0%,#e6d6bf 22%,#d4bc9c 55%,#bfa17e 100%)}
.hero-title{position:absolute;left:83px;top:186px;font-family:"Cormorant Garamond",serif;font-weight:400;font-size:50px;line-height:52px;color:var(--ink)}
.hero-lead{position:absolute;left:83px;top:340px;width:470px;font-size:15px;line-height:25px;color:var(--ink)}
.hero-actions{position:absolute;left:83px;top:447px;display:flex;gap:17px}
.btn-olive{background:var(--olive);color:#fff;width:209px}
.btn-outline{border:1px solid var(--ink);width:209px;color:var(--ink)}
.features{position:absolute;left:83px;top:627px;width:1034px;height:130px;background:#fff;display:flex;align-items:center;padding:0 32px;box-shadow:0 6px 24px rgba(0,0,0,.05)}
.feature{flex:1;display:flex;align-items:center;gap:20px}
.feature-icon{width:66px;height:66px;border-radius:50%;background:var(--beige);display:flex;align-items:center;justify-content:center;flex:none}
.feature h3{font-size:13px;font-weight:500;margin-bottom:6px}
.feature p{font-size:11px;line-height:17px;color:var(--muted)}

/* visa */
.visa{top:800px;height:598px;background:var(--olive);color:#fff}
.visa .label{position:absolute;left:83px;top:83px;color:#b7bda9}
.visa h2{position:absolute;left:83px;top:118px;font-family:"Cormorant Garamond",serif;font-weight:400;font-size:38px;line-height:42px}
.visa h2 em{color:var(--tan)}
.rule{position:absolute;width:84px;height:1px;background:var(--tan)}
.visa .intro{position:absolute;left:83px;top:252px;width:380px;font-size:12.5px;line-height:20px;color:#e2e4da}
.btn-tan{background:var(--tan);color:#fff;width:192px}
.visa .btn-tan{position:absolute;left:83px;top:376px}
.visa-card{position:absolute;width:242px;background:var(--olive-card);padding:26px 24px}
.visa-card h3{font-size:12px;font-weight:500;letter-spacing:.3px;text-transform:uppercase;margin:22px 0 10px}
.visa-card p,.visa-card li{font-size:11px;line-height:18px;color:#dfe2d6}
.visa-card ul{list-style:none}
.visa-card li{padding-left:20px;position:relative;margin-bottom:4px}
.visa-card li::before{content:"";position:absolute;left:2px;top:5px;width:7px;height:4px;border-left:1px solid #dfe2d6;border-bottom:1px solid #dfe2d6;transform:rotate(-45deg)}

/* featured */
.featured{top:1398px;height:475px;background:#fff}
.featured-photo{position:absolute;left:0;top:0;width:600px;height:475px;background:linear-gradient(90deg,#c9a882 0%,#d9c2a2 55%,#efe6da 88%,#fff 100%)}
.tag{position:absolute;left:14px;top:18px;background:var(--dark);color:#fff;font-size:8.5px;letter-spacing:.8px;padding:5px 9px;border-radius:12px}
.featured .label{position:absolute;left:642px;top:44px}
.featured h2{position:absolute;left:642px;top:84px;font-family:"Cormorant Garamond",serif;font-weight:400;font-size:40px;letter-spacing:1px}
.featured .lead{position:absolute;left:642px;top:146px;width:480px;font-size:12.5px;line-height:20px}
.facts{position:absolute;left:642px;top:218px;display:flex;gap:34px}
.fact{display:flex;gap:10px}
.fact b{display:block;font-family:"Cormorant Garamond",serif;font-weight:500;font-size:16px;color:var(--muted)}
.fact span{font-size:10.5px;color:var(--muted)}
.featured .btn-outline{position:absolute;left:642px;top:378px;width:192px}

/* duo */
.duo{top:1880px;height:372px}
.invest{position:absolute;left:8px;top:0;width:587px;height:372px;background:var(--dark);color:#fff;padding:40px 42px}
.invest .label,.partner .label{color:#b1a896}
.duo h2{font-family:"Cormorant Garamond",serif;font-weight:400;font-size:38px;line-height:40px;margin-top:16px}
.invest h2 em{color:var(--tan)}
.invest .desc{font-size:12px;line-height:19px;margin-top:32px;width:270px;color:#ddd6cc}
.link{position:absolute;font-size:11px;letter-spacing:.5px;text-transform:uppercase;display:flex;align-items:center;gap:10px}
.invest .link{left:42px;top:296px;color:var(--tan)}
.step{position:absolute;left:357px;width:200px}
.step .num{width:42px;height:42px;border-radius:50%;border:1px solid #6a6359;display:flex;align-items:center;justify-content:center;font-family:"Cormorant Garamond",serif;font-size:20px}
.step h3{font-size:12px;font-weight:400;letter-spacing:.5px;color:var(--tan);margin:14px 0 6px}
.step p{font-size:12px;line-height:19px;color:#e6e0d6}
.partner{position:absolute;left:605px;top:0;width:587px;height:372px;background:linear-gradient(90deg,#f3ece2 0%,#efe4d5 45%,#d7c2a5 100%);padding:40px 42px}
.partner .desc{font-size:12px;line-height:19px;margin-top:32px;width:240px}
.partner .link{left:42px;top:296px}

/* news */
.news{top:2252px;height:733px;background:var(--beige)}
.news .label{position:absolute;left:83px;top:90px}
.news h2{position:absolute;left:83px;top:110px;font-family:"Cormorant Garamond",serif;font-weight:400;font-size:40px;line-height:42px}
.news .sub{position:absolute;left:505px;top:120px;width:330px;font-size:12px;line-height:20px;color:#8f877c}
.news .btn-outline{position:absolute;left:908px;top:112px;width:209px}
.card{position:absolute;top:236px;width:334px;height:412px;background:#fff}
.card-photo{height:183px}
.card-body{padding:24px 25px}
.card-meta{display:flex;justify-content:space-between;font-size:10.5px;color:var(--muted)}
.card h3{font-family:"Cormorant Garamond",serif;font-weight:500;font-size:21px;line-height:24px;margin:16px 0 10px}
.card p{font-size:12px;line-height:19px}
.card .link{left:25px;top:370px;color:var(--tan);font-size:9.5px}

/* contact */
.contact{top:2985px;height:655px;background:var(--olive);color:#fff}
.contact .label{position:absolute;left:83px;top:90px;color:#b7bda9}
.contact h2{position:absolute;left:83px;top:118px;font-family:"Cormorant Garamond",serif;font-weight:400;font-size:38px;line-height:40px}
.contact h2 em{color:var(--tan)}
.contact .intro{position:absolute;left:83px;top:258px;width:340px;font-size:12.5px;line-height:20px;color:#e2e4da}
.info{position:absolute;left:83px;width:330px;display:flex;gap:16px;padding-bottom:14px;border-bottom:1px solid rgba(255,255,255,.15)}
.info b{display:block;font-weight:400;color:var(--tan);font-size:12px;margin-bottom:3px}
.info span{font-size:12.5px}
.chats{position:absolute;left:83px;top:540px;display:flex;gap:16px;align-items:center;font-size:11px;color:#c9cdbd}
.chat{display:flex;align-items:center;gap:10px}
.chat i{width:38px;height:38px;border-radius:50%;background:var(--tan);display:block}
.form{position:absolute;left:458px;top:83px;width:659px;height:487px;background:#fff;padding:42px 42px;color:var(--ink)}
.form label{display:block;font-size:10.5px;letter-spacing:1.2px;text-transform:uppercase;margin-bottom:12px}
.field{background:#f4f1ec;border:1px solid #e7e1d8;height:48px;font-size:12px;color:#9a9288;padding:0 12px;display:flex;align-items:center}
.row{display:flex;gap:22px;margin-bottom:26px}
.row>div{flex:1}
.textarea{height:106px;align-items:flex-start;padding-top:14px}
.agree{display:flex;align-items:center;gap:12px;font-size:12px;margin-top:26px}
.box{width:20px;height:20px;background:var(--olive);display:flex;align-items:center;justify-content:center}
.agree a{color:var(--tan);text-decoration:none}
.secure{font-size:9px;color:#9a9288;margin-top:16px}
.form .btn-tan{position:absolute;right:42px;top:394px;width:209px}

/* footer */
.site-footer{top:3640px;height:260px;background:var(--beige);border-top:1px solid var(--line)}
.foot-brand{position:absolute;left:83px;top:50px;text-align:center}
.foot-brand .brand-mark{margin:0 auto 8px}
.socials{display:flex;gap:14px;margin-top:18px}
.socials i{width:24px;height:24px;border-radius:50%;background:#8b847a;display:block}
.col{position:absolute;top:44px;font-size:11.5px;line-height:26px}
.col h4{font-size:10.5px;letter-spacing:1.5px;font-weight:400;color:var(--muted);text-transform:uppercase;margin-bottom:10px}
.col .ln{display:flex;gap:12px;align-items:flex-start;line-height:18px;margin-bottom:8px}
.vr{position:absolute;top:48px;width:1px;height:170px;background:var(--line)}
.flag{display:inline-block;width:16px;height:10px;margin-right:8px;vertical-align:-1px}
.chat-fab{position:absolute;left:1130px;top:172px;width:54px;height:54px;border-radius:50%;background:var(--tan);display:flex;align-items:center;justify-content:center}
.legal-bar{top:3900px;height:125px;background:var(--stone);font-size:8.5px;line-height:13px;color:var(--muted)}
.legal-bar b{font-weight:600}
.badges{position:absolute;left:290px;top:28px;display:grid;grid-template-columns:110px 110px;gap:14px}
.badge{display:flex;align-items:center;gap:8px}
.badge i{width:24px;height:24px;border-radius:50%;border:1px solid #b8ad9e;display:block}
.badge span{display:block;width:50px;height:5px;background:#c2b8aa}
</style>
</head>
<body>

<header class="site-header">
  <div class="brand"><span class="brand-mark"></span><span class="brand-name">VELTAROON</span></div>
  <nav class="nav"><span>Golden Visa</span><span>Projects</span><span>Investors</span><span>Partners</span><span>Contact</span></nav>
  <div class="login">CLIENT LOGIN
    <svg width="14" height="14" viewBox="0 0 14 14" fill="none" stroke="#2a2824"><circle cx="7" cy="4.5" r="3"/><path d="M1.5 13c.8-3 3-4.5 5.5-4.5s4.7 1.5 5.5 4.5"/></svg></div>
  <div class="lang">EN &nbsp;⌄</div>
</header>

<section class="hero">
  <div class="hero-photo" role="img" aria-label="Sunlit living room with beige sofa, olive tree and open terrace overlooking a Greek island bay"></div>
  <h1 class="hero-title">Premium Greek Living<br><em>&amp; Golden Visa Investments</em></h1>
  <p class="hero-lead">Boutique real estate projects in Greece that open the door to European residency through the Greek Golden Visa.</p>
  <div class="hero-actions">
    <span class="btn btn-olive">Explore Visa <svg class="arrow" viewBox="0 0 20 8" fill="none" stroke="#fff"><path d="M0 4h19M15 1l4 3-4 3"/></svg></span>
    <span class="btn btn-outline">Explore Projects <svg class="arrow" viewBox="0 0 20 8" fill="none" stroke="#2a2824"><path d="M0 4h19M15 1l4 3-4 3"/></svg></span>
  </div>
  <div class="features">
    <div class="feature"><div class="feature-icon"><svg width="26" height="26" viewBox="0 0 26 26" fill="none" stroke="#6d665d"><rect x="5" y="3" width="14" height="19"/><path d="M8 8h8M8 12h8M8 16h5"/><circle cx="19" cy="19" r="4"/></svg></div><div><h3>Greek Golden Visa</h3><p>Residency for you and<br>your family</p></div></div>
    <div class="feature"><div class="feature-icon"><svg width="26" height="26" viewBox="0 0 26 26" fill="none" stroke="#6d665d"><path d="M3 22h20M5 22V10l7-5 7 5v12M10 22v-6h6v6"/></svg></div><div><h3>Boutique Projects</h3><p>Carefully selected and<br>renovated properties</p></div></div>
    <div class="feature"><div class="feature-icon"><svg width="26" height="26" viewBox="0 0 26 26" fill="none" stroke="#6d665d"><path d="M4 12l9-7 9 7M7 10v10h12V10"/><path d="M10 16h6"/></svg></div><div><h3>Rental Management</h3><p>Full-service support<br>for investors</p></div></div>
    <div class="feature"><div class="feature-icon"><svg width="26" height="26" viewBox="0 0 26 26" fill="none" stroke="#6d665d"><circle cx="13" cy="13" r="9"/><path d="M4 15c4-2 14-2 18 0M13 4v4"/></svg></div><div><h3>Mediterranean Living</h3><p>Enjoy a lifestyle like<br>no other</p></div></div>
  </div>
</section>

<section class="visa">
  <div class="label">Greek Golden Visa</div>
  <h2>Your European future<br>starts in <em>Greece</em></h2>
  <div class="rule" style="left:83px;top:226px"></div>
  <p class="intro">Invest in qualifying real estate and secure residency for you and your family with one of Europe's most attractive programs</p>
  <span class="btn btn-tan">Learn More <svg class="arrow" viewBox="0 0 20 8" fill="none" stroke="#fff"><path d="M0 4h19M15 1l4 3-4 3"/></svg></span>
  <div class="visa-card" style="left:625px;top:83px;height:210px">
    <svg width="28" height="28" viewBox="0 0 28 28" fill="none" stroke="#dfe2d6"><path d="M3 10l11-6 11 6M5 10v12M11 10v12M17 10v12M23 10v12M2 24h24"/></svg>
    <h3>Investment Threshold</h3><p>From €250,000 in qualified real estate</p></div>
  <div class="visa-card" style="left:875px;top:83px;height:210px">
    <svg width="34" height="28" viewBox="0 0 34 28" fill="none" stroke="#dfe2d6"><circle cx="7" cy="5" r="3"/><circle cx="27" cy="5" r="3"/><circle cx="17" cy="12" r="2.5"/><path d="M3 26V12h8v14M23 26V12h8v14M14 26v-9h6v9"/></svg>
    <h3>Who Can Apply</h3><p>Main applicant, spouse, children under 21, and parents of both spouses</p></div>
  <div class="visa-card" style="left:625px;top:303px;height:212px">
    <svg width="28" height="28" viewBox="0 0 28 28" fill="none" stroke="#dfe2d6"><path d="M14 2l10 4v8c0 6-5 10-10 12C9 24 4 20 4 14V6z"/><path d="M10 14l3 3 5-6"/></svg>
    <h3>Key Benefits</h3><ul><li>EU Residency for the family</li><li>Visa-free Schengen travel</li><li>No minimum stay requirement</li><li>Pathway to permanent residency</li></ul></div>
  <div class="visa-card" style="left:875px;top:303px;height:212px">
    <svg width="28" height="28" viewBox="0 0 28 28" fill="none" stroke="#dfe2d6"><path d="M5 2h12l5 5v11M5 2v24h10"/><path d="M9 10h8M9 14h8M9 18h4"/><circle cx="21" cy="22" r="3"/></svg>
    <h3>Turnkey Solution</h3><p>We handle everything: property, legal, paperwork and after-sales support</p></div>
</section>

<section class="featured">
  <div class="featured-photo" role="img" aria-label="Terraced cream stone residential building with balconies and greenery at sunset"></div>
  <span class="tag">FEATURED PROJECT</span>
  <div class="label">Featured Project</div>
  <h2>MORVILO LIVING</h2>
  <p class="lead">A boutique residential building in the heart of Athens, designed for modern living and smart investment</p>
  <div class="facts">
    <div class="fact"><svg width="16" height="20" viewBox="0 0 16 20" fill="none" stroke="#6d665d"><path d="M8 19s6-6 6-11A6 6 0 0 0 2 8c0 5 6 11 6 11z"/><circle cx="8" cy="8" r="2"/></svg><div><b>Prime Location</b><span>Koukaki, Athens</span></div></div>
    <div class="fact"><svg width="20" height="18" viewBox="0 0 20 18" fill="none" stroke="#6d665d"><path d="M2 8l8-6 8 6M4 7v10h12V7M8 17v-5h4v5"/></svg><div><b>Boutique Residences</b><span>1 &amp; 2 Bedroom Units</span></div></div>
    <div class="fact"><svg width="18" height="20" viewBox="0 0 18 20" fill="none" stroke="#6d665d"><circle cx="9" cy="8" r="6"/><path d="M6 13l-2 6 5-2 5 2-2-6"/></svg><div><b>Golden Visa</b><span>Eligible</span></div></div>
  </div>
  <span class="btn btn-outline">View Project <svg class="arrow" viewBox="0 0 20 8" fill="none" stroke="#2a2824"><path d="M0 4h19M15 1l4 3-4 3"/></svg></span>
</section>

<section class="duo">
  <div class="invest">
    <div class="label">Invest with Veltaroon</div>
    <h2>Stable returns<br>for a <em>secure future</em></h2>
    <p class="desc">Two proven investment models designed for long-term value and peace of mind</p>
    <span class="link">For Investors <svg class="arrow" viewBox="0 0 20 8" fill="none" stroke="#c6a07a"><path d="M0 4h19M15 1l4 3-4 3"/></svg></span>
    <div class="step" style="top:42px"><div class="num">01</div><h3>INVEST IN PROJECTS</h3><p>10–15% annual returns from development projects</p></div>
    <div class="step" style="top:198px"><div class="num">02</div><h3>BUY &amp; EARN</h3><p>5% annual rental income guaranteed for the first 3 years</p></div>
  </div>
  <div class="partner" role="img" aria-label="Seaside terrace with infinity pool and lounge sofa overlooking a green bay">
    <div class="label">Partner with us</div>
    <h2>Grow together<br>in Greece</h2>
    <div class="rule" style="left:42px;top:170px"></div>
    <p class="desc">Join our partner network and offer your clients premium real estate solutions with attractive commissions</p>
    <span class="link">Become a Partner <svg class="arrow" viewBox="0 0 20 8" fill="none" stroke="#2a2824"><path d="M0 4h19M15 1l4 3-4 3"/></svg></span>
  </div>
</section>

<section class="news">
  <div class="label">News &amp; Insights</div>
  <h2>Stay informed.<br>Make <em>smarter decisions.</em></h2>
  <p class="sub">Expert insights, market updates, and company news to keep you ahead in the Greek real estate market</p>
  <span class="btn btn-outline">View All Articles <svg class="arrow" viewBox="0 0 20 8" fill="none" stroke="#2a2824"><path d="M0 4h19M15 1l4 3-4 3"/></svg></span>
  <article class="card" style="left:83px">
    <div class="card-photo" role="img" aria-label="Modern white apartment building with terraces and trees" style="background:linear-gradient(135deg,#d9d2c6,#b7a88f)"></div>
    <div class="card-body"><div class="card-meta"><span>Market Insights</span><span>May 20, 2026</span></div>
      <h3>Why Greece remains a top investment destination in 2026</h3>
      <p>Stable economy, growing demand, and strategic location make Greece a smart long-term choice</p></div>
    <span class="link">Read More <svg class="arrow" viewBox="0 0 20 8" fill="none" stroke="#c6a07a"><path d="M0 4h19M15 1l4 3-4 3"/></svg></span>
  </article>
  <article class="card" style="left:433px">
    <div class="card-photo" role="img" aria-label="Passport and residency card on a table with a whitewashed island village behind" style="background:linear-gradient(135deg,#eef0f2,#c7d0d8)"></div>
    <div class="card-body"><div class="card-meta"><span>Golden Visa</span><span>April 3, 2026</span></div>
      <h3>Greek Golden Visa: Everything you need to know</h3>
      <p>Key changes, benefits, and a step-by-step guide to obtaining your residency</p></div>
    <span class="link">Read More <svg class="arrow" viewBox="0 0 20 8" fill="none" stroke="#c6a07a"><path d="M0 4h19M15 1l4 3-4 3"/></svg></span>
  </article>
  <article class="card" style="left:783px">
    <div class="card-photo" role="img" aria-label="Warm wooden open-plan living and dining interior" style="background:linear-gradient(135deg,#d8c5a8,#a8895f)"></div>
    <div class="card-body"><div class="card-meta"><span>Investment Strategy</span><span>June 14, 2026</span></div>
      <h3>Why Greece remains a top investment destination in 2026</h3>
      <p>Stable economy, growing demand, and strategic location make Greece a smart long-term choice</p></div>
    <span class="link">Read More <svg class="arrow" viewBox="0 0 20 8" fill="none" stroke="#c6a07a"><path d="M0 4h19M15 1l4 3-4 3"/></svg></span>
  </article>
</section>

<section class="contact">
  <div class="label">Get in Touch</div>
  <h2>Let's Build Your<br><em>Secure Future</em></h2>
  <div class="rule" style="left:83px;top:226px"></div>
  <p class="intro">Our team is here to guide you through every step of your investment journey in Greece</p>
  <div class="info" style="top:345px"><svg width="16" height="18" viewBox="0 0 16 20" fill="none" stroke="#c6a07a"><path d="M8 19s6-6 6-11A6 6 0 0 0 2 8c0 5 6 11 6 11z"/><circle cx="8" cy="8" r="2"/></svg><div><b>Address</b><span>Irinis Kyprou 14, Athens 117 42, Greece</span></div></div>
  <div class="info" style="top:408px"><svg width="16" height="16" viewBox="0 0 16 16" fill="none" stroke="#c6a07a"><path d="M3 1h3l1.5 4-2 1.2a9 9 0 0 0 4.3 4.3L11 8.5l4 1.5v3a2 2 0 0 1-2 2A13 13 0 0 1 1 3a2 2 0 0 1 2-2z"/></svg><div><b>Phone</b><span>+30 210 555 01 84</span></div></div>
  <div class="info" style="top:471px;border:0"><svg width="16" height="14" viewBox="0 0 16 14" fill="none" stroke="#c6a07a"><rect x="1" y="1" width="14" height="12"/><path d="M1 2l7 6 7-6"/></svg><div><b>Email</b><span>info@veltaroon.gr</span></div></div>
  <div class="chats"><span class="chat"><i></i>Instant Chat</span><span class="chat"><i></i>Web Chat</span><span class="chat"><i></i>Messenger</span></div>
  <div class="form">
    <div class="row"><div><label>Full Name</label><div class="field">Your full name</div></div><div><label>Email</label><div class="field">Your email address</div></div></div>
    <div class="row"><div><label>Phone Number</label><div class="field">Your phone number</div></div></div>
    <div><label>Phone Number</label><div class="field textarea">Tell us about your investment goals...</div></div>
    <div class="agree"><span class="box"><svg width="10" height="8" viewBox="0 0 10 8" fill="none" stroke="#fff" stroke-width="1.5"><path d="M1 4l3 3 5-6"/></svg></span>I agree to the <a>Privacy Policy</a></div>
    <p class="secure">✓ &nbsp;Your information is securely processed and never shared with third parties</p>
    <span class="btn btn-tan">Send Message</span>
  </div>
</section>

<footer class="site-footer">
  <div class="foot-brand"><span class="brand-mark" style="display:block"></span><span class="brand-name" style="font-size:18px">VELTAROON</span>
    <div class="socials"><i></i><i></i><i></i></div></div>
  <div class="col" style="left:274px"><h4>Golden Visa</h4><div>Investment Benefits</div><div>Buy &amp; Earn Program</div><div>Rental Guarantee</div><div>How It Works</div><div>Documents &amp; Resources</div><div>FAQ</div></div>
  <div class="vr" style="left:460px"></div>
  <div class="col" style="left:519px"><h4>Contact</h4>
    <div class="ln"><svg width="11" height="14" viewBox="0 0 16 20" fill="none" stroke="#6d665d"><path d="M8 19s6-6 6-11A6 6 0 0 0 2 8c0 5 6 11 6 11z"/></svg><span>Irinis Kyprou 14,<br>Athens 117 42, Greece</span></div>
    <div class="ln"><svg width="12" height="12" viewBox="0 0 16 16" fill="none" stroke="#6d665d"><path d="M3 1h3l1.5 4-2 1.2a9 9 0 0 0 4.3 4.3L11 8.5l4 1.5v3a2 2 0 0 1-2 2A13 13 0 0 1 1 3a2 2 0 0 1 2-2z"/></svg><span>+30 210 555 01 84</span></div>
    <div class="ln"><svg width="12" height="10" viewBox="0 0 16 14" fill="none" stroke="#6d665d"><rect x="1" y="1" width="14" height="12"/><path d="M1 2l7 6 7-6"/></svg><span>info@veltaroon.gr</span></div>
    <div class="ln"><svg width="12" height="12" viewBox="0 0 12 12" fill="none" stroke="#6d665d"><circle cx="6" cy="6" r="5"/><path d="M6 3v3l2 1"/></svg><span>Mon – Fri: 09:00 – 18:00 (EET)</span></div></div>
  <div class="vr" style="left:763px"></div>
  <div class="col" style="left:823px"><h4>Legal</h4><div>Privacy Policy</div><div>Cookie Policy</div><div>Terms &amp; Conditions</div><div>GDPR Compliance</div></div>
  <div class="vr" style="left:983px"></div>
  <div class="col" style="left:1043px"><h4>Language</h4>
    <div><span class="flag" style="background:#2d3f7a"></span>English</div>
    <div><span class="flag" style="background:linear-gradient(#3c6bb5 50%,#fff 50%)"></span>Ελληνικά</div>
    <div><span class="flag" style="background:linear-gradient(#fff 33%,#2e52a5 33% 66%,#c8302a 66%)"></span>Русский</div>
    <div><span class="flag" style="background:#c8302a"></span>中文</div>
    <div><span class="flag" style="background:#d3202a"></span>Türkçe</div></div>
  <div class="chat-fab"><svg width="24" height="22" viewBox="0 0 24 22" fill="none" stroke="#fff" stroke-width="1.4"><path d="M12 2C6.5 2 2 5.8 2 10.5c0 2.3 1 4.3 2.8 5.9L4 21l4.7-2.4c1 .3 2.1.4 3.3.4 5.5 0 10-3.8 10-8.5S17.5 2 12 2z"/></svg></div>
</footer>

<section class="legal-bar">
  <div style="position:absolute;left:83px;top:28px;width:190px"><b>VELTAROON DEVELOPMENT IKE</b><br>G.E.MI. No: 000000000000<br>VAT No: EL000000000<br>DOY: A' ATHENS<br>Licensed Real Estate Developer in Greece</div>
  <div class="badges"><div class="badge"><i></i><span></span></div><div class="badge"><i></i><span></span></div><div class="badge"><i></i><span></span></div><div class="badge"><i></i><span></span></div></div>
  <div style="position:absolute;left:587px;top:28px;width:530px"><b>DISCLAIMER</b><br>The information on this website is for general information purposes only and does not constitute investment advice. All investments involve risk. Past performance is not indicative of future results.<br><br>© 2024 Veltaroon Development IKE. All rights reserved.</div>
</section>

</body>
</html>
```